Golf Brochure + Business Card Design Project – Larchmere Wellness.

Task Description

We are looking for a premium tri-fold brochure (8.5x11 letter, folded) plus a new business card design for Larchmere Wellness. Both need to look polished, elegant, and professional — something that would feel at home in a golf club environment.

Brochure Scope:
• Tri-fold brochure promoting our new golf-specific services
• Incorporate brand colors: deep hunter green, cream, and gold accents
• Clean, modern typography (professional, not playful)
• Layout will follow the copy provided (final copy attached, no rewriting needed)
• Imagery: mature golfers (50+), golf lifestyle shots, no generic stocky images
• Include QR code placement linking to booking page
• Deliverables: print-ready PDF with bleed/crop (CMYK), high-res PDF (digital), and source file (InDesign or Illustrator)

Business Card Scope:
• Front + back design
• Consistent with brand colors and fonts
• Space for name, title, phone, email, and website
• Deliverables: print-ready PDF with bleed/crop (CMYK) + source file (AI or InDesign)
• If possible, provide editable template for future staff cards

Timeline:
• First draft within 5–7 days
• 2 rounds of revisions included

Budget:
$300 USD (total for both brochure + business card)

I’ll provide finalized copy if you accept the project.
Project description (paste this whole block in that box)

We need a premium tri-fold brochure (8.5”×11” letter, folded) and a new business card design for Larchmere Wellness. This will be presented to golf course managers and members, so the look must be elegant, restrained, and country-club-classy.

Scope — Brochure
• Format: Tri-fold, 8.5”×11”. Please set 0.125” bleed on all sides and keep critical text ≥0.125–0.25” inside the trim.
• Purpose: Promote Larchmere Wellness’ golf-specific services for adults 50+.
• Copy: We will provide finalized copy in a Word doc after acceptance. No rewriting needed — please focus on layout and polish.
• Imagery (required):
• Golf-first images (ball on tee/green, mature golfers mid-swing, and golf course landscapes at golden hour).
• 1–2 real Larchmere Wellness gym photos on inside panels (trainer with client doing golf-relevant movement: stretch, rotation, balance).
• Visual style: Premium, quiet, lots of white/negative space, balanced grids; no clutter.
• Brand colors (required): Hunter Green #0C2E1F, Gold #CBA135, Cream #F5F2EB. Convert for CMYK print while preserving the look.
• Typography: Clean, legible serif + sans pairing (e.g., modern serif for headlines, humanist/neo-grotesk sans for body). You may propose suitable professional fonts; avoid playful/novelty fonts.
• Elements to include:
• Our logo (we will upload).
• QR code placement to booking page (we will supply the URL / QR asset).
• Simple icon treatment for the three complimentary options (Strength & Mobility, Stretch Therapy, Corelyn + Assessment).
• Deliverables:
• Print-ready PDF (CMYK, with bleed & crop marks, PDF/X-1a or PDF/X-4)
• High-res digital PDF (no bleed)
• Source file (InDesign or Illustrator) + packaged fonts/links or outlined type as appropriate.

Scope — Business Card
• Size: 3.5”×2” (US standard) with 0.125” bleed; keep text ≥0.125” from trim.
• Front/back design; consistent with brochure branding.
• Fields: Name, Title, Phone, Email, Website, Address; optional small QR on back.
• Deliverables: Print-ready PDF (CMYK, bleed & crops) + Source file (AI/INDD). Provide an editable template for staff names.

Process & Timing
• Initial concept for brochure + card within 5–7 days of acceptance.
• 2 rounds of revisions included.
• Please start with a clean layout concept using placeholder images/text blocks; we’ll drop in final copy/assets immediately after acceptance.

Stock & Licensing
• You may propose stock images that fit the brief (we’re fine approving Pictavault or equivalent). Please note any license fees separately if needed.

Usage Rights
• We require full usage rights to the final designs for print & digital.

Target Market(s)

Golfers 50+ in Victoria, BC: quality-oriented, health-conscious, want to play longer, stronger, and pain-free. Country-club aesthetic; expect polished, professional materials.

Industry/Entity Type

Health & Fitness — Golf Performance / Longevity Studio

Font styles to use
Serif
Sans Serif

Requirements
Must have
• • Golf-first imagery + 1–2 real Larchmere Wellness photos inside. • Brand colors: #0C2E1F (Hunter Green), #CBA135 (Gold), #F5F2EB (Cream). • Premium, restrained layout; ample negative space; no clutter. • Clean professional serif + sans type pairing; highly legible. • Space for logo and QR code (booking). • Correct print specs (bleed, crops, CMYK). • Deliverables: print-ready PDFs (brochure + card), digital PDF, source files.
Nice to have
• • Subtle texture or grain in backgrounds (very light) to add sophistication. • A second brochure cover variation (ball on tee vs. course landscape) at concept stage.
Should not have
• • Cheesy/posed “stocky” groups; overly young models; beer/alcohol imagery. • Over-saturated greens/blues; gimmicky gradients or clip art. • Generic fitness/bodybuilding shots unrelated to golf performance.

```html
<!DOCTYPE html>
<html lang="en">
<head>
<meta charset="utf-8">
<title>Larchmere Wellness – Business Card</title>
<link rel="stylesheet" href="https://fonts.googleapis.com/css2?family=Playfair+Display:wght@400;700&family=Inter:wght@400&display=swap">
<style>
  :root {
    --backdrop: #bdbdbd;
    --hunter: #0b2a1e;
    --gold: #c9a235;
    --cream: #f7f6f0;
    --ink: #111111;
    --rule: #8a8a86;
  }
  * { margin: 0; padding: 0; box-sizing: border-box; }
  html, body { width: 1200px; height: 1200px; overflow: hidden; }
  body { background: var(--backdrop); position: relative; }

  .card { position: absolute; left: 262px; width: 676px; height: 386px; }
  .card--front { top: 189px; background: var(--hunter); }
  .card--back { top: 625px; background: var(--cream); }

  .brand-mark { position: absolute; display: flex; flex-direction: column; align-items: center; }
  .brand-mark__ring { border-radius: 50%; border-style: solid; }
  .brand-mark__name { font-family: "Playfair Display", serif; font-weight: 700; text-align: center; line-height: 1.15; }

  .card--front .brand-mark { left: 0; right: 0; top: 52px; }
  .card--front .brand-mark__ring { width: 96px; height: 96px; border-width: 4px; border-color: var(--gold); }
  .card--front .brand-mark__name { color: var(--gold); font-size: 36px; margin-top: 26px; }

  .tagline {
    position: absolute; left: 0; right: 0; top: 316px; text-align: center;
    font-family: "Playfair Display", serif; font-size: 22px; color: #ffffff; letter-spacing: 0.2px;
  }

  .card--back .brand-mark { left: 48px; width: 210px; top: 104px; }
  .card--back .brand-mark__ring { width: 76px; height: 76px; border-width: 3px; border-color: var(--hunter); }
  .card--back .brand-mark__name { color: var(--hunter); font-size: 25px; margin-top: 18px; }

  .divider { position: absolute; left: 285px; top: 83px; width: 1px; height: 221px; background: var(--rule); }

  .contact { position: absolute; left: 319px; top: 82px; }
  .contact__name { font-family: "Playfair Display", serif; font-weight: 700; font-size: 31px; color: var(--ink); line-height: 1.2; }
  .contact__title { font-family: "Inter", sans-serif; font-size: 18px; color: var(--ink); margin-top: 6px; }
  .contact__title .bar { display: inline-block; width: 1px; height: 20px; background: var(--ink); vertical-align: -4px; margin: 0 6px; }

  .contact__list { list-style: none; margin-top: 21px; }
  .contact__item { display: flex; align-items: center; height: 34px; margin-bottom: 14.5px;
    font-family: "Inter", sans-serif; font-size: 18.5px; color: var(--ink); }
  .contact__icon { width: 34px; height: 34px; margin-right: 10px; flex: none; }
</style>
</head>
<body>
  <section class="card card--front">
    <div class="brand-mark">
      <div class="brand-mark__ring"></div>
      <div class="brand-mark__name">Larchmere Wellness</div>
    </div>
    <p class="tagline">• Strength • Mobility • Longevity</p>
  </section>

  <section class="card card--back">
    <div class="brand-mark">
      <div class="brand-mark__ring"></div>
      <div class="brand-mark__name">Larchmere<br>Wellness</div>
    </div>
    <div class="divider"></div>
    <div class="contact">
      <h1 class="contact__name">Mara-Lynn Ashford</h1>
      <p class="contact__title">Owner<span class="bar"></span>Larchmere Wellness</p>
      <ul class="contact__list">
        <li class="contact__item">
          <svg class="contact__icon" viewBox="0 0 34 34" aria-hidden="true">
            <circle cx="17" cy="17" r="16" fill="var(--hunter)" stroke="var(--hunter)"/>
            <circle cx="17" cy="17" r="14" fill="none" stroke="#f7f6f0" stroke-width="0.8"/>
            <path d="M11 10.5l2.5-1 2 4-1.5 1.2c.8 2 2.2 3.4 4.2 4.2l1.2-1.5 4 2-1 2.5c-5.5.3-11.7-5.9-11.4-11.4z" fill="none" stroke="#f7f6f0" stroke-width="1"/>
            <path d="M19 9.5a5.5 5.5 0 0 1 5.5 5.5M19 12a3 3 0 0 1 3 3" fill="none" stroke="#f7f6f0" stroke-width="0.9"/>
          </svg>
          250-555-0148
        </li>
        <li class="contact__item">
          <svg class="contact__icon" viewBox="0 0 34 34" aria-hidden="true">
            <circle cx="17" cy="17" r="16" fill="var(--hunter)"/>
            <circle cx="17" cy="17" r="14" fill="none" stroke="#f7f6f0" stroke-width="0.8"/>
            <rect x="10" y="13" width="14" height="10" fill="none" stroke="#f7f6f0" stroke-width="1"/>
            <path d="M10 13l7 5.5 7-5.5M10 23l5.5-5M24 23l-5.5-5" fill="none" stroke="#f7f6f0" stroke-width="1"/>
          </svg>
          mara@larchmerewellness.biz
        </li>
        <li class="contact__item">
          <svg class="contact__icon" viewBox="0 0 34 34" aria-hidden="true">
            <circle cx="17" cy="17" r="16" fill="var(--hunter)"/>
            <circle cx="17" cy="17" r="14" fill="none" stroke="#f7f6f0" stroke-width="0.8"/>
            <circle cx="17" cy="17" r="7.5" fill="none" stroke="#f7f6f0" stroke-width="1"/>
            <ellipse cx="17" cy="17" rx="3.2" ry="7.5" fill="none" stroke="#f7f6f0" stroke-width="1"/>
            <path d="M9.5 17h15M10.5 13.5h13M10.5 20.5h13" fill="none" stroke="#f7f6f0" stroke-width="0.9"/>
          </svg>
          larchmerewellnessvictoria.com
        </li>
      </ul>
    </div>
  </section>
</body>
</html>
```